House Cleaning company in need of handout re-designs

We are looking to create a 2 sided, full color, 6" x 4" handout that promotes the company www.brisvale.com

We have one in existence that performed well, but find it too busy and would like another one designed to test performance (please see the attached files for original design). We are looking for one additional design, however depending on quality of work submitted we will select up to 5 designs.

We are looking for clean designs the will improve performance and you are 'carte blanche' on the design. That said, please ensure the following elements are present:

1) Space for an offer (i.e $39 for 3 hours of cleaning) with an expiry date.
2) Unique URL
3) Promo Code
4) Phone Number
5) The tagline of "Let Brisvale handle it" is present.
6) Logo
7) Brand colors are maintained

Also, please highlight the following:

*Eco-Friendly Cleaning Services
*Fully-Screened Cleaning Experts
*60-point checklist
*Easy Online Booking Process

Thank you.

```html
<!DOCTYPE html>
<html lang="en">
<head>
<meta charset="utf-8">
<title>Brisvale Handout</title>
<link href="https://fonts.googleapis.com/css2?family=Oswald:wght@400;500;600&family=Roboto:wght@400;500;700&display=swap" rel="stylesheet">
<style>
  :root {
    --coral: #ef6a63;
    --teal: #22bdb0;
    --teal-light: #7fd6cf;
    --ink: #444444;
    --white: #ffffff;
    --frame: #d9d9d9;
    --stage: #2b2b2b;
    --tick: #f5d33a;
  }
  * { margin: 0; padding: 0; box-sizing: border-box; }
  html, body { width: 1200px; height: 1000px; overflow: hidden; }
  body { background: var(--stage); position: relative; font-family: "Roboto", Arial, sans-serif; }

  .card {
    position: absolute; left: 273px; width: 655px; height: 436px;
    background: var(--white); border: 8px solid var(--frame); overflow: hidden;
  }
  .card--front { top: 55px; }
  .card--back { top: 510px; }
  .card > * { position: absolute; }

  /* front */
  .front-kicker { left: 19px; top: 18px; font: 400 30px/1 "Oswald", sans-serif; color: var(--ink); white-space: nowrap; transform: scaleX(0.88); transform-origin: left top; z-index: 2; }
  .front-headline { left: 19px; top: 42px; font: 400 86px/1 "Oswald", sans-serif; color: var(--coral); white-space: nowrap; transform: scaleX(0.80); transform-origin: left top; z-index: 2; }
  .photo-cleaner { left: -6px; top: 100px; width: 228px; height: 330px; background: linear-gradient(180deg, #eef6f6 0%, #3fbfb2 70%, #2aa79b 100%); border-radius: 110px 110px 0 0; z-index: 1; }
  .photo-kitchen { left: 206px; top: 134px; width: 160px; height: 160px; border-radius: 50%; border: 4px solid var(--white); box-shadow: 0 0 0 2px #cfcfcf; background: linear-gradient(160deg, #f2f2f0 0%, #d9d2c6 55%, #b98552 100%); }
  .bubble-tail { left: 430px; top: 40px; }
  .photo-family { left: 443px; top: 50px; width: 192px; height: 192px; border-radius: 50%; border: 4px solid var(--white); box-shadow: 0 0 0 2px #cfcfcf; background: linear-gradient(160deg, #fafafa 0%, #e9d8c9 50%, #c9a98a 100%); }
  .dot { border-radius: 50%; }
  .dot--teal { left: 378px; top: 138px; width: 30px; height: 30px; background: var(--teal); }
  .dot--ring { left: 414px; top: 142px; width: 16px; height: 16px; border: 2px solid var(--teal); }
  .dot--yellow { left: 366px; top: 166px; width: 12px; height: 12px; background: #e9e07a; }

  .contact { right: 22px; text-align: right; white-space: nowrap; }
  .book-now { top: 266px; font: 400 22px/1 "Oswald", sans-serif; color: var(--ink); }
  .brand-inline { color: var(--coral); font-weight: 600; }
  .unique-url { top: 301px; font: 700 27px/1 "Roboto", sans-serif; color: var(--teal); }
  .phone { top: 336px; font: 700 27px/1 "Roboto", sans-serif; color: var(--teal); }
  .phone-or { color: var(--ink); font-weight: 400; }
  .divider { left: 319px; top: 374px; width: 300px; border-top: 2px dotted #9a9a9a; }
  .promo { top: 387px; font: 400 16px/1 "Roboto", sans-serif; color: var(--ink); }
  .promo sup { font-size: 9px; }

  /* back */
  .panel { left: 0; top: 0; }
  .logo { left: 19px; top: 30px; font: 600 42px/1 "Oswald", sans-serif; color: var(--coral); }
  .intro { left: 19px; top: 96px; width: 212px; font: 400 14.5px/18.2px "Roboto", sans-serif; color: var(--ink); }
  .tagline { left: 297px; top: 22px; font: 500 42px/1.1 "Oswald", sans-serif; color: var(--white); text-transform: uppercase; }
  .features { left: 297px; top: 126px; list-style: none; }
  .features li { font: 700 18.5px/30px "Roboto", sans-serif; color: var(--white); display: flex; align-items: center; gap: 6px; }
  .coupon { left: 21px; top: 264px; width: 598px; height: 135px; background: var(--coral); }
  .coupon-border { position: absolute; inset: 5px; border: 2px dashed var(--white); }
  .coupon-price { position: absolute; left: 14px; top: 2px; font: 600 110px/1 "Oswald", sans-serif; color: var(--white); }
  .coupon-price sup { font-size: 48px; vertical-align: 46px; }
  .coupon-title { position: absolute; left: 189px; top: 14px; font: 500 40px/1 "Oswald", sans-serif; color: var(--white); }
  .coupon-terms { position: absolute; left: 189px; top: 64px; font: 400 19px/26px "Roboto", sans-serif; color: var(--white); }
</style>
</head>
<body>

<section class="card card--front">
  <div class="photo-kitchen" role="img" aria-label="Photo of a bright clean kitchen"></div>
  <svg class="bubble-tail" width="230" height="260" viewBox="0 0 230 260">
    <path d="M175 195 L222 250 L150 218 Z" fill="#ffffff" stroke="#cfcfcf" stroke-width="2"/>
  </svg>
  <div class="photo-family" role="img" aria-label="Photo of a happy family with their dog"></div>
  <span class="dot dot--teal"></span>
  <span class="dot dot--ring"></span>
  <span class="dot dot--yellow"></span>
  <div class="photo-cleaner" role="img" aria-label="Photo of a smiling cleaner in a teal apron holding a mop and bucket"></div>
  <p class="front-kicker">DO YOU REALLY HAVE THE TIME TO TACKLE</p>
  <h1 class="front-headline">HOUSE CHORES?</h1>

  <p class="contact book-now">BOOK NOW AT <span class="brand-inline">Brisvale.com</span></p>
  <p class="contact unique-url">www.brisvale.com/ca39</p>
  <p class="contact phone"><span class="phone-or">or</span> call1-800-555-0139</p>
  <div class="divider"></div>
  <p class="contact promo">A <sup>$</sup>105 Value! Use Promo Code: CA39</p>
</section>

<section class="card card--back">
  <svg class="panel" width="639" height="420" viewBox="0 0 639 420">
    <path d="M255 0 Q300 200 345 420 L639 420 L639 0 Z" fill="#7fd6cf"/>
    <path d="M270 0 Q320 200 365 420 L639 420 L639 0 Z" fill="#22bdb0"/>
  </svg>
  <p class="logo">Brisvale.com</p>
  <p class="intro">Brisvale professionals provide thorough, eco-friendly cleaning services that make your home sparkling clean! Each fully-screened cleaning expert follows a 60-point checklist to ensure spotless results for your home!</p>
  <h2 class="tagline">Let Brisvale<br>handle it!</h2>
  <ul class="features">
    <li><svg width="16" height="16" viewBox="0 0 16 16"><path d="M2 9 L6 13 L14 3" fill="none" stroke="#f5d33a" stroke-width="3" stroke-linecap="round"/></svg>Eco-Friendly Cleaning Services</li>
    <li><svg width="16" height="16" viewBox="0 0 16 16"><path d="M2 9 L6 13 L14 3" fill="none" stroke="#f5d33a" stroke-width="3" stroke-linecap="round"/></svg>Fully-Screened Cleaning Experts</li>
    <li><svg width="16" height="16" viewBox="0 0 16 16"><path d="M2 9 L6 13 L14 3" fill="none" stroke="#f5d33a" stroke-width="3" stroke-linecap="round"/></svg>60-point checklist</li>
    <li><svg width="16" height="16" viewBox="0 0 16 16"><path d="M2 9 L6 13 L14 3" fill="none" stroke="#f5d33a" stroke-width="3" stroke-linecap="round"/></svg>Easy Online Booking Process</li>
  </ul>
  <div class="coupon">
    <div class="coupon-border"></div>
    <p class="coupon-price"><sup>$</sup>39</p>
    <p class="coupon-title">CLEANING FOR 3 HOURS</p>
    <p class="coupon-terms">Offer good for first time cleaning.<br>Offers expires 11/30/2014</p>
  </div>
</section>

</body>
</html>
```